Copper lark buildworks

Copper lark buildworks is a small construction company.
Who is a licenced builder, Carpenter, joiner,
working on heritage ,new build, speacial projects and sometimes furniture

Industry/Entity Type

Construction

```html
<!DOCTYPE html>
<html lang="en">
<head>
<meta charset="utf-8">
<title>Copper Lark Buildworks — Business Card</title>
<link rel="stylesheet" href="https://fonts.googleapis.com/css2?family=Source+Sans+3:wght@400;600;700&display=swap">
<style>
  :root {
    --backdrop: #8c8c8f;
    --card-centre: #232428;
    --card-edge: #111115;
    --frame-green: #1f9a45;
    --frame-green-deep: #15713a;
    --title-green: #3a7d3f;
    --name-green: #3f7e42;
    --ornament-light: #27a64c;
    --ornament-deep: #0f5f2c;
  }
  * { margin: 0; padding: 0; box-sizing: border-box; }
  html, body {
    width: 1200px;
    height: 1200px;
    overflow: hidden;
    background: var(--backdrop);
  }
  .card {
    position: absolute;
    left: 20px;
    top: 272px;
    width: 1160px;
    height: 656px;
    background: radial-gradient(ellipse at 50% 48%, var(--card-centre) 0%, #1d1e22 45%, var(--card-edge) 100%);
  }
  .card__frame {
    position: absolute;
    inset: 0;
    width: 1160px;
    height: 656px;
  }
  .card__ornament {
    position: absolute;
    left: 368px;
    width: 425px;
    border-radius: 40px;
    background: radial-gradient(ellipse at 50% 50%, var(--ornament-light) 0%, rgba(21, 113, 58, 0.55) 45%, rgba(15, 95, 44, 0) 78%);
    opacity: 0.55;
  }
  .card__ornament--top { top: 186px; height: 66px; }
  .card__ornament--bottom { top: 402px; height: 68px; }
  .card__company {
    position: absolute;
    left: 0;
    right: 0;
    top: 276px;
    text-align: center;
    font-family: "Source Sans 3", "Myriad Pro", sans-serif;
    font-weight: 700;
    font-size: 44px;
    line-height: 52px;
    letter-spacing: 0.2px;
    color: var(--title-green);
    text-transform: uppercase;
  }
  .card__person {
    position: absolute;
    left: 0;
    right: 0;
    top: 347px;
    text-align: center;
    font-family: "Source Sans 3", "Myriad Pro", sans-serif;
    font-weight: 400;
    font-size: 34px;
    line-height: 40px;
    color: var(--name-green);
  }
</style>
</head>
<body>
  <main class="card">
    <svg class="card__frame" viewBox="0 0 1160 656" xmlns="http://www.w3.org/2000/svg" aria-hidden="true">
      <defs>
        <linearGradient id="frameStroke" x1="0" y1="0" x2="1" y2="1">
          <stop offset="0" stop-color="var(--frame-green)"/>
          <stop offset="0.6" stop-color="var(--frame-green)"/>
          <stop offset="1" stop-color="var(--frame-green-deep)"/>
        </linearGradient>
      </defs>
      <polygon class="frame-outer" points="133,69 1027,69 1092,134 1092,522 1027,587 133,587 68,522 68,134"
               fill="none" stroke="url(#frameStroke)" stroke-width="3"/>
      <polygon class="frame-inner" points="137,81 1023,81 1080,138 1080,518 1023,575 137,575 80,518 80,138"
               fill="none" stroke="url(#frameStroke)" stroke-width="3"/>
      <line class="rule rule--top" x1="335" y1="258" x2="825" y2="258" stroke="var(--frame-green)" stroke-width="3"/>
      <line class="rule rule--bottom" x1="335" y1="396" x2="825" y2="396" stroke="var(--frame-green)" stroke-width="3"/>
    </svg>

    <div class="card__ornament card__ornament--top" role="img" aria-label="Decorative green flourish above the company name"></div>
    <h1 class="card__company">Copper Lark Buildworks</h1>
    <p class="card__person">Mara Quill</p>
    <div class="card__ornament card__ornament--bottom" role="img" aria-label="Decorative green flourish below the name"></div>
  </main>
</body>
</html>
```